Fundraising Event Logistics and Strategy

We need a web design for our non-profit fundraising event strategy business. We help non-profits streamline gala and 'pre registered' event operations to maximize their funds raised. We would like a simple design, our company colors are dark blue and silver. The design should be clean and also allow for some partner logos. I have attached some current logo collateral. Company is Dana Whitcombe & Co dba BidHarbors, but neither logo has to be used.
Target Market(s)
Non Profit Organizations
Industry/Entity Type
Business
Number of Pages Required
3 page
Requirements
Must have
- Contact Us Form
- Partner Logos with Links

```html
<!DOCTYPE html>
<html lang="en">
<head>
<meta charset="utf-8">
<title>Dana Whitcombe &amp; Co dba BidHarbors</title>
<link rel="stylesheet" href="https://fonts.googleapis.com/css2?family=Open+Sans:wght@400;600;700&display=swap">
<style>
:root{
  --blue:#1e5fab;
  --blue-dark:#174b88;
  --navy:#1f2b38;
  --navy-deep:#18222d;
  --silver:#eceef1;
  --silver-mid:#d5d9de;
  --ink:#333a42;
  --muted:#7a828b;
  --white:#ffffff;
}
*{margin:0;padding:0;box-sizing:border-box}
html,body{width:1200px;height:2516px;overflow:hidden}
body{font-family:"Open Sans",Arial,sans-serif;color:var(--ink);background:var(--white);font-size:13px}
.topbar{height:32px;background:var(--blue);color:var(--white);display:flex;justify-content:space-between;align-items:center;padding:0 60px;font-size:12px}
.topbar span{display:flex;align-items:center;gap:8px}
.header{height:96px;display:flex;justify-content:space-between;align-items:center;padding:0 60px;border-bottom:1px solid var(--silver-mid)}
.brand{display:flex;align-items:center;gap:10px;font-size:17px;font-weight:600;color:var(--navy)}
.brand i{width:34px;height:34px;border-radius:50%;background:var(--silver-mid);display:block}
.nav{display:flex;gap:26px;font-size:13px}
.nav a{color:var(--ink);text-decoration:none;padding-bottom:6px}
.nav a.active{color:var(--blue);border-bottom:2px solid var(--blue)}
.hero{height:472px;position:relative;background:linear-gradient(100deg,#c9ced6 0%,#eef0f3 35%,#f7f8fa 55%,#b9c3d6 70%,#e3e6ec 100%);display:flex;align-items:center;justify-content:center}
.hero h1{font-size:46px;font-weight:400;color:rgba(255,255,255,.92);letter-spacing:1px;text-shadow:0 1px 3px rgba(0,0,0,.25);margin-top:80px}
.section-title{font-size:28px;font-weight:400;text-align:center;color:var(--ink)}
.about{height:230px;padding-top:36px;text-align:center}
.about p{width:720px;margin:18px auto 20px;font-size:12px;line-height:1.6;color:var(--muted)}
.btn{display:inline-block;background:var(--blue);color:var(--white);font-size:12px;padding:7px 18px;border-radius:2px}
.services{height:310px;background:var(--silver);margin-top:14px;display:flex;justify-content:center;gap:84px;padding-top:38px}
.service{width:204px;text-align:center}
.service .icon{width:84px;height:84px;border-radius:50%;background:var(--blue);margin:0 auto 18px;display:flex;align-items:center;justify-content:center;box-shadow:0 0 0 5px #d7dee8}
.service h3{font-size:15px;font-weight:600;color:var(--blue);margin-bottom:8px}
.service p{font-size:11px;line-height:1.55;color:var(--muted);margin-bottom:10px}
.service .more{font-size:11px;font-weight:600;color:var(--ink)}
.why{height:380px;padding-top:36px}
.cards{display:flex;justify-content:center;gap:22px;margin-top:28px}
.card{width:214px;box-shadow:0 3px 8px rgba(0,0,0,.18);background:var(--white)}
.card .photo{height:160px}
.card .photo.a{background:linear-gradient(135deg,#c8ccc4,#9aa08e)}
.card .photo.b{background:linear-gradient(135deg,#8aa36c,#c4c9a2)}
.card .photo.c{background:linear-gradient(135deg,#d9c7a7,#a6b6c2)}
.card p{font-size:11px;text-align:center;padding:12px 16px;line-height:1.45;color:var(--ink)}
.card.featured p{background:var(--blue);color:var(--white)}
.partners{height:230px;padding-top:20px}
.logos{display:flex;justify-content:center;align-items:center;gap:54px;margin-top:36px}
.logos span{display:block;background:#8c939b}
.contact{height:480px;display:flex}
.location{width:580px;background:var(--blue);color:var(--white);padding:48px 0 0 170px}
.location h2,.form h2{font-size:24px;font-weight:400;margin-bottom:22px}
.location h2{border-bottom:1px solid rgba(255,255,255,.35);padding-bottom:12px;width:300px}
.location h4{font-size:13px;font-weight:600;margin:14px 0 8px}
.addr{display:flex;gap:10px;font-size:11px;line-height:1.6}
.form{flex:1;background:var(--silver);padding:48px 0 0 40px}
.form h2{color:var(--ink);border-bottom:1px solid var(--silver-mid);padding-bottom:12px;width:360px}
.field{width:360px;height:26px;background:var(--white);border:1px solid var(--silver-mid);margin-bottom:10px;font-size:11px;color:var(--muted);padding:5px 8px}
.field.area{height:30px}
.captcha{font-size:11px;margin:4px 0 8px}
.send{display:inline-block;background:var(--blue);color:var(--white);font-size:12px;padding:8px 26px;margin-top:6px}
.footer{height:220px;background:var(--navy);color:#c4cbd3;display:flex;padding:38px 0 0 120px;font-size:11px}
.col{width:250px}
.col h5{color:var(--white);font-size:13px;font-weight:600;margin-bottom:12px}
.col li{list-style:none;margin-bottom:7px}
.col li::before{content:"›";margin-right:8px;color:#7fa8d8}
.line{display:flex;gap:8px;margin-bottom:10px;line-height:1.5}
.mini{width:170px;height:22px;background:var(--white);margin:8px 0;border-radius:1px}
.submit{display:inline-block;background:var(--blue);color:var(--white);padding:4px 12px;font-size:11px}
.bottombar{height:36px;background:var(--navy-deep);color:#9aa3ad;font-size:11px;display:flex;justify-content:space-between;align-items:center;padding:0 120px}
.social{display:flex;gap:8px}
.social i{width:16px;height:16px;border-radius:50%;background:#4b5663;display:block}
</style>
</head>
<body>
<div class="topbar">
  <span><svg width="14" height="10" viewBox="0 0 14 10"><rect x=".5" y=".5" width="13" height="9" fill="none" stroke="#fff"/><path d="M.5 .5 7 6l6.5-5.5" fill="none" stroke="#fff"/></svg>dwhitcombe@bidharbors.com</span>
  <span><svg width="12" height="12" viewBox="0 0 12 12"><path d="M2 1h2l1 3-1.5 1a7 7 0 0 0 3.5 3.5L8 7l3 1v2c0 1-1 1-1 1C5 11 1 7 1 2c0 0 0-1 1-1z" fill="#fff"/></svg>727-555-0148</span>
</div>
<header class="header">
  <div class="brand"><i></i>Dana Whitcombe &amp; Co</div>
  <nav class="nav"><a class="active">Home</a><a>Who We Are</a><a>Why Choose Us</a><a>News</a><a>Contact</a></nav>
</header>
<section class="hero" role="img" aria-label="Photo of an hourglass on a desk with business people shaking hands in the background">
  <h1>We are Happy to Help</h1>
</section>
<section class="about">
  <h2 class="section-title">Who We Are</h2>
  <p>It is a long established fact that a reader will be distracted by the readable content of a page when looking at its layout. The point of using Lorem Ipsum is that it has a more-or-less normal distribution of letters, as opposed to using 'Content here, content here', making it look like readable English.</p>
  <span class="btn">Read More</span>
</section>
<section class="services">
  <div class="service">
    <div class="icon"><svg width="40" height="40" viewBox="0 0 40 40" fill="#fff"><circle cx="14" cy="12" r="5"/><circle cx="27" cy="12" r="5"/><path d="M5 30c0-6 4-10 9-10s9 4 9 10zM19 30c0-6 3-10 8-10s8 4 8 10z"/></svg></div>
    <h3>Consulting</h3>
    <p>It is a long established fact that a reader will be distracted by the readable content.</p>
    <span class="more">Read More »</span>
  </div>
  <div class="service">
    <div class="icon"><svg width="40" height="40" viewBox="0 0 40 40"><rect x="10" y="7" width="20" height="26" fill="none" stroke="#fff" stroke-width="2.5"/><path d="M14 15h12M14 20h12M14 25h8" stroke="#fff" stroke-width="2"/></svg></div>
    <h3>Responsibility</h3>
    <p>It is a long established fact that a reader will be distracted by the readable content.</p>
    <span class="more">Read More »</span>
  </div>
  <div class="service">
    <div class="icon"><svg width="40" height="40" viewBox="0 0 40 40" fill="#fff"><circle cx="20" cy="9" r="5"/><path d="M13 34V18h14v16h-4v-9h-6v9z"/><path d="M27 18l7-8" stroke="#fff" stroke-width="2.5"/></svg></div>
    <h3>Success</h3>
    <p>It is a long established fact that a reader will be distracted by the readable content.</p>
    <span class="more">Read More »</span>
  </div>
</section>
<section class="why">
  <h2 class="section-title">Why Choose Us</h2>
  <div class="cards">
    <div class="card"><div class="photo a" role="img" aria-label="Photo of volunteers sorting donations"></div><p>5 Millennial Donor Engagement Strategies That Work</p></div>
    <div class="card featured"><div class="photo b" role="img" aria-label="Photo of hands joined together outdoors"></div><p>5 Millennial Donor Engagement Strategies That Work</p></div>
    <div class="card"><div class="photo c" role="img" aria-label="Photo of a smiling couple at a charity event"></div><p>5 Millennial Donor Engagement Strategies That Work</p></div>
  </div>
</section>
<section class="partners">
  <h2 class="section-title">Our Partners</h2>
  <div class="logos">
    <span style="width:56px;height:56px;border-radius:50%"></span>
    <span style="width:110px;height:46px"></span>
    <span style="width:100px;height:46px"></span>
    <span style="width:52px;height:52px"></span>
  </div>
</section>
<section class="contact">
  <div class="location">
    <h2>Location</h2>
    <h4>Dana Whitcombe &amp; Co dba</h4>
    <div class="addr"><svg width="10" height="14" viewBox="0 0 10 14"><path d="M5 0a5 5 0 0 1 5 5c0 4-5 9-5 9S0 9 0 5a5 5 0 0 1 5-5z" fill="#fff"/><circle cx="5" cy="5" r="2" fill="#1e5fab"/></svg><div>Gala Planning Group<br>310 Bayview Lane<br>Suite 4B<br>Clearwater FL 33755</div></div>
    <h4 style="margin-top:26px">Co dba BidHarbors</h4>
    <div class="addr"><svg width="10" height="14" viewBox="0 0 10 14"><path d="M5 0a5 5 0 0 1 5 5c0 4-5 9-5 9S0 9 0 5a5 5 0 0 1 5-5z" fill="#fff"/><circle cx="5" cy="5" r="2" fill="#1e5fab"/></svg><div>Gala Planning Group<br>310 Bayview Lane<br>Suite 4B<br>Clearwater FL 33755</div></div>
  </div>
  <div class="form">
    <h2>Contact Us</h2>
    <div class="field">Name</div>
    <div class="field">Email</div>
    <div class="field">Phone</div>
    <div class="field area"></div>
    <div class="captcha">Please Enter CAPTCHA: <b>W8</b></div>
    <div class="field"></div>
    <span class="send">SEND</span>
  </div>
</section>
<footer class="footer">
  <div class="col"><h5>Main menu</h5><ul><li>Home</li><li>Who We Are</li><li>Why Choose Us</li><li>News</li><li>Contact</li></ul></div>
  <div class="col"><h5>Information</h5><ul><li>Partners</li><li>Legal Notice</li><li>Terms and Conditions</li><li>Security and Privacy</li><li>Payment Methods</li></ul></div>
  <div class="col"><h5>Contact us</h5>
    <div class="line"><svg width="10" height="14" viewBox="0 0 10 14"><path d="M5 0a5 5 0 0 1 5 5c0 4-5 9-5 9S0 9 0 5a5 5 0 0 1 5-5z" fill="#c4cbd3"/></svg><span>1420 Harbor Point Drive, Suite 200<br>Tampa, FL 33607</span></div>
    <div class="line"><svg width="12" height="12" viewBox="0 0 12 12"><path d="M2 1h2l1 3-1.5 1a7 7 0 0 0 3.5 3.5L8 7l3 1v2c0 1-1 1-1 1C5 11 1 7 1 2c0 0 0-1 1-1z" fill="#c4cbd3"/></svg><span>727-555-0148</span></div>
    <div class="line"><svg width="14" height="10" viewBox="0 0 14 10"><rect x=".5" y=".5" width="13" height="9" fill="none" stroke="#c4cbd3"/><path d="M.5 .5 7 6l6.5-5.5" fill="none" stroke="#c4cbd3"/></svg><span>dwhitcombe@bidharbors.com</span></div>
  </div>
  <div class="col"><h5>Quick Contact</h5><div>Leave your email here for updates</div><div class="mini"></div><span class="submit">Submit</span></div>
</footer>
<div class="bottombar">
  <span>© 2024 BidHarbors. All rights reserved.</span>
  <div class="social"><i></i><i></i><i></i><i></i><i></i></div>
</div>
</body>
</html>
```